A paperback book cover entitled: The Quiet Ledger

1. For the front cover of the paperback I need the photo of me walking down the driveway at Wattlebrook Manor as the focal point. The designer will use their discretion where to insert the book title: The Quiet Ledger.
Also the designer will use their discretion where my name Desmond Farrow as the author is placed. Attached is a contemporary photo of me to use if the designer thinks that possible. Both these photos are attached.
2. The back cover page will contain two main written insertions (1) About the Book and (2) About the Author.
The book will be an 8.5x11 inch paperback of some 570 pages published by Pelibrix.
About the book:
This book is about Australian Public Affairs 1957-2020 as perceived and observed by Desmond Farrow. It has a significant but not exclusive Queensland focus concerning History, Commentary, and Anecdotes, plus some things Desmond has been involved with along the way.
Desmond developed unique Transition to Government and Transition to Opposition plans that have all been implemented. Some of those plans are referred to in the book and other Transition plans are appendixes to the book.
Now at 73 years of age, Desmond’s motivation for writing this book is to ensure a wealth of historical scenarios are captured and incorporated into the public record for future generations.

About the author:

Desmond Farrow has been a largely silent and invisible political confidant to Australian Premiers and Prime Ministers.
Desmond worked in the Queensland public sector from 1971-2009 as Chief of Staff to four Queensland State Opposition Leaders for 13 years and then as a Public Sector senior executive.
He subsequently served on the Edith Carrow Trust Board, the Harbourline Reading Institute Board, and consulted to a mining company. He has recorded many Oral History projects for The Calder Archive in Canberra.
Over the last 30+ years, he has been approached countless times for advice relating to Business, Government, Authors, Historians, and people seeking a job. He has never charged a cent for any of his advice, even when not working within Government.
There are two extra photos attached to maybe be on each side at the bottom of the back cover if the designer thinks it is appropriate.
Those in the 4 person photo from the left were all connected with the Tarrington Assembly: former Civic Minister Neil Ostrow, Former Heartland Party Premier Rod Linsey, former Reform Leader Glen Harker, and Desmond Farrow

In the three person photo from the left are: Desmond Farrow, Former PM Bernard Coldwell, and Prime Minister Lionel Parsk.

3. In the spine of the book will be simply (1) The Quiet Ledger and (2) Desmond Farrow

Here’s hoping a good design is created.

```html
<!DOCTYPE html>
<html lang="en">
<head>
<meta charset="utf-8">
<title>The Quiet Ledger — Book Cover</title>
<link rel="stylesheet" href="https://fonts.googleapis.com/css2?family=Anton&family=Source+Sans+3:wght@400;600&display=swap">
<style>
  :root {
    --cover-red: #8b1a0f;
    --map-black: #050505;
    --ink-white: #ffffff;
    --photo-bw: #9a9a96;
    --photo-warm: #c9b48a;
    --photo-room: #b7b2aa;
    --portrait: #4a4c52;
  }
  * { margin: 0; padding: 0; box-sizing: border-box; }
  html, body { width: 1200px; height: 838px; overflow: hidden; background: var(--cover-red); }
  .cover {
    position: relative; width: 1200px; height: 838px; overflow: hidden;
    background: var(--cover-red); color: var(--ink-white);
    font-family: "Source Sans 3", "Myriad Pro", sans-serif;
  }
  .map-silhouette {
    position: absolute; left: 150px; top: 34px; width: 1030px; height: 770px;
    background: var(--map-black);
    border-radius: 46% 40% 44% 52% / 38% 44% 50% 46%;
  }
  .display {
    position: absolute; font-family: "Anton", Impact, sans-serif; font-weight: 400;
    color: var(--ink-white); line-height: 1; text-transform: uppercase;
    -webkit-text-stroke: 1.5px #000; paint-order: stroke fill;
    white-space: nowrap;
  }
  /* back cover */
  .back-kicker { left: 196px; top: 30px; font-size: 28px; }
  .back-title { left: 53px; top: 57px; font-size: 155px; letter-spacing: -2px; }
  .back-copy { position: absolute; left: 54px; width: 462px; font-size: 10.4px; line-height: 1.3; }
  .about-book { top: 216px; }
  .about-book .gap { margin-top: 13px; }
  .photo { position: absolute; }
  .photo-group-four { left: 96px; top: 362px; width: 148px; height: 97px; background: linear-gradient(160deg, #d9d6cf, var(--photo-room) 60%, #6d6a66); }
  .photo-group-three { left: 311px; top: 362px; width: 138px; height: 97px; background: linear-gradient(160deg, #e3cf9d, var(--photo-warm) 55%, #5b4a2f); }
  .caption { position: absolute; top: 469px; font-size: 7.4px; line-height: 1.3; text-align: center; }
  .caption-four { left: 50px; width: 240px; }
  .caption-three { left: 280px; width: 210px; }
  .about-author-heading { position: absolute; left: 54px; width: 404px; top: 516px; text-align: center; font-size: 10.6px; font-weight: 400; letter-spacing: 0.3px; }
  .author-intro { position: absolute; left: 53px; top: 539px; font-size: 8.6px; white-space: nowrap; }
  .author-portrait { left: 54px; top: 556px; width: 74px; height: 94px; border: 1px solid #ddd; background: linear-gradient(180deg, #8d9098, var(--portrait)); }
  .author-bio { position: absolute; left: 133px; top: 556px; width: 370px; font-size: 8.4px; line-height: 1.3; }
  .author-bio .gap { margin-top: 10px; }
  /* spine */
  .spine-name { left: 580px; top: 64px; font-size: 39px; writing-mode: vertical-rl; letter-spacing: 0.5px; -webkit-text-stroke: 0; }
  .spine-kicker { left: 626px; top: 336px; font-size: 22px; writing-mode: vertical-rl; -webkit-text-stroke: 0; }
  .spine-title { left: 548px; top: 440px; font-size: 112px; writing-mode: vertical-rl; letter-spacing: -2px; }
  /* front cover */
  .front-kicker { left: 694px; top: 116px; font-size: 54px; -webkit-text-stroke: 0; }
  .front-title { left: 696px; top: 178px; font-size: 153px; letter-spacing: -1px; }
  .photo-driveway { left: 706px; top: 400px; width: 152px; height: 220px; transform: rotate(-6deg); background: linear-gradient(170deg, #e4e4df, var(--photo-bw) 55%, #3a3a38); border: 3px solid #f2f2ee; }
  .photo-front-three { left: 932px; top: 374px; width: 216px; height: 144px; transform: rotate(-20deg); background: linear-gradient(150deg, #ead7a5, var(--photo-warm) 55%, #4e3f27); box-shadow: 2px 3px 6px rgba(0,0,0,.5); }
  .photo-front-four { left: 826px; top: 494px; width: 200px; height: 150px; background: linear-gradient(160deg, #dedbd4, var(--photo-room) 60%, #67645f); }
  .front-author { left: 718px; top: 676px; font-size: 54px; letter-spacing: 0.5px; -webkit-text-stroke: 0; }
</style>
</head>
<body>
<main class="cover">
  <div class="map-silhouette" role="img" aria-label="Black silhouette map of Australia spanning the wrap"></div>

  <section class="back-cover">
    <div class="display back-kicker">The Quiet</div>
    <h1 class="display back-title">Ledger</h1>

    <div class="back-copy about-book">
      <p>This book is about Australian Public Affairs 1957-2020 as perceived and observed by Desmond Farrow.</p>
      <p class="gap">It has a significant but not exclusive Queensland focus concerning History, Commentary, and Anecdotes, plus some things Desmond has been involved with along the way.</p>
      <p>Desmond developed unique Transition to Government and Transition to Opposition plans that have all been implemented.</p>
      <p>Some of those plans are referred to in the book and other Transition plans are appendixes to the book.</p>
      <p class="gap">Now at 73 years of age, Desmond’s motivation for writing this book is to ensure a wealth of historical scenarios are captured and incorporated into the public record for future generations.</p>
    </div>

    <div class="photo photo-group-four" role="img" aria-label="Photo of four men standing together in a dining room"></div>
    <div class="photo photo-group-three" role="img" aria-label="Signed photo of three men, one seated"></div>
    <p class="caption caption-four">Civic Minister Neil Ostrow, Heartland Party Premier Rod Linsey,<br>Reform Leader Glen Harker, and Desmond Farrow</p>
    <p class="caption caption-three">Desmond Farrow,<br>Former PM Bernard Coldwell, and Prime Minister Lionel Parsk.</p>

    <h2 class="about-author-heading">ABOUT THE AUTHOR</h2>
    <p class="author-intro">Desmond Farrow has been a largely silent and invisible political confidant to Australian Premiers and Prime Ministers.</p>
    <div class="photo author-portrait" role="img" aria-label="Portrait photo of the author"></div>
    <div class="author-bio">
      <p>Desmond worked in the Queensland public sector from 1971-2009 as Chief of Staff to four Queensland State Opposition Leaders for 13 years and then as a Public Sector senior executive. He subsequently served on the Edith Carrow Trust Board, the Harbourline Reading Institute Board, and consulted to a mining company. He has recorded many Oral History projects for The Calder Archive in Canberra.</p>
      <p class="gap">Over the last 30+ years, he has been approached countless times for advice relating to Business, Government, Authors, Historians, and people seeking a job.</p>
      <p>He has never charged a cent for any of his advice, even when not working within Government.</p>
    </div>
  </section>

  <section class="spine">
    <div class="display spine-name">Desmond Farrow</div>
    <div class="display spine-kicker">The Quiet</div>
    <div class="display spine-title">Ledger</div>
  </section>

  <section class="front-cover">
    <div class="display front-kicker">The Quiet</div>
    <div class="display front-title">Ledger</div>
    <div class="photo photo-driveway" role="img" aria-label="Black and white photo of the author walking down the driveway at Wattlebrook Manor"></div>
    <div class="photo photo-front-three" role="img" aria-label="Signed colour photo of three men"></div>
    <div class="photo photo-front-four" role="img" aria-label="Photo of four men standing together in a dining room"></div>
    <div class="display front-author">Desmond Farrow</div>
  </section>
</main>
</body>
</html>
```